The Willow Hours - a modern wellness brand

Looking for a modern, simple, and clean website for a virtual consulting firm focused on holistic wellness and sustainable living. Want a strong combo of text and photos (really shitty starts are available for reference on www.thewillowhours.com and www.helenabrusco.com for reference - general idea is in the right direction, was too difficult to work through with the wordpress template and nothing laid out correctly)
Needs include:
- strong home / landing page
- ability to schedule (use calend.ly) on the site
- online shop / purchasing POS integration
- blog
-multiple 'services' pages
- about page
- contact page
(attached brand board images for brand style / reference)
Updates
Want more opportunity for designs and feedback
Target Market(s)
women and gay men aged 30-50
Coding
Coded - Design and coding required
Number of Pages Required
5+ page
Colors
Designer to choose only greyscale colors for use in the design.
Requirements
Must have
- the ability for me to update and manage through wordpress when things like pricing, or services change
Should not have
- complicated anything

```html
<!DOCTYPE html>
<html lang="en">
<head>
<meta charset="utf-8">
<title>The Willow Hours</title>
<link rel="stylesheet" href="https://fonts.googleapis.com/css2?family=Cinzel:wght@400;500;600&family=Roboto:wght@400;500;700&display=swap">
<style>
:root{
  --ink:#111111;
  --white:#ffffff;
  --text:#6a6a6a;
  --muted:#8a8a8a;
  --hero-1:#8a8a8a;
  --hero-2:#5a5a5a;
  --hero-3:#2e2e2e;
  --stone-1:#f3f3f3;
  --stone-2:#e6e6e6;
  --stone-3:#c9c9c9;
}
*{margin:0;padding:0;box-sizing:border-box}
html,body{width:1200px;height:4000px;overflow:hidden;background:var(--white)}
body{position:relative;font-family:'Roboto',sans-serif;color:var(--ink)}
.abs{position:absolute}
.bands{position:absolute;left:0;top:0;width:1200px;height:4000px}

/* header */
.brand{position:absolute;text-align:center;font-family:'Cinzel',serif;color:var(--ink);letter-spacing:4px}
.brand-mark{display:block;margin:0 auto;border:1.5px solid var(--ink);border-radius:50%}
.brand-name{display:block;font-size:24px;line-height:1.1;font-weight:500}
.brand-sub{display:block;font-size:12px;letter-spacing:14px;margin-right:-14px}
.phone{position:absolute;display:flex;align-items:center;gap:8px;font-size:21px;color:var(--ink)}
.phone-icon{width:30px;height:30px;border-radius:50%;background:var(--ink);display:flex;align-items:center;justify-content:center}
.btn{position:absolute;display:flex;align-items:center;justify-content:center;background:var(--ink);color:var(--white);border-radius:30px;font-size:11px;font-weight:700;text-transform:uppercase}
.nav{position:absolute;top:80px;left:624px;font-size:14px;font-weight:500}
.nav a{position:absolute;color:var(--ink);text-decoration:none;white-space:nowrap}
.cart{position:absolute;left:1015px;top:76px}

/* hero */
.hero-title{position:absolute;left:0;width:1200px;text-align:center;font-family:'Cinzel',serif;color:var(--white)}
.hero-title .big{display:block;font-size:104px;font-weight:500;letter-spacing:26px;margin-right:-26px;line-height:1}
.hero-title .small{display:block;font-size:58px;letter-spacing:54px;margin-right:-54px;margin-top:22px;line-height:1}

/* headings */
.section-title{position:absolute;left:0;width:1200px;text-align:center;font-family:'Cinzel',serif;font-size:62px;font-weight:600;color:var(--ink);line-height:1}
.section-title .dash{display:inline-block;width:52px;height:2px;background:currentColor;vertical-align:middle;margin:0 12px}

/* about */
.about-photo{position:absolute;left:166px;top:1021px;width:366px;height:366px;border-radius:50%;background:linear-gradient(135deg,#dcdcdc,#a0a0a0 45%,#505050)}
.about-ring{position:absolute;left:150px;top:1005px;width:398px;height:398px;border-radius:50%;border:2px solid var(--ink)}
.about-title{position:absolute;left:598px;top:990px;font-family:'Cinzel',serif;font-size:62px;font-weight:600;line-height:1}
.about-title .dash{display:inline-block;width:50px;height:2px;background:var(--ink);vertical-align:middle;margin:0 6px}
.about-text{position:absolute;left:601px;top:1076px;width:448px;font-size:13.4px;line-height:26.4px;color:var(--text);text-align:justify}

/* services */
.service{position:absolute;width:286px;height:286px;border:3px solid var(--ink);border-radius:50%;text-align:center}
.service-icon{position:absolute;left:113px;top:22px}
.service h3{position:absolute;top:102px;left:0;width:100%;font-size:19px;font-weight:700;color:var(--ink)}
.service p{position:absolute;top:136px;left:46px;width:188px;font-size:13px;line-height:24px;color:var(--muted)}
.service-arrow{position:absolute;left:124px;top:264px;width:38px;height:38px;border-radius:50%;background:var(--ink);display:flex;align-items:center;justify-content:center}

/* blog */
.post-photo{position:absolute;width:440px;height:271px}
.post-card{position:absolute;width:371px;height:255px;background:var(--white);box-shadow:0 2px 10px rgba(0,0,0,.12);padding:30px 32px}
.post-meta{display:flex;align-items:center;gap:8px;font-size:12.5px;color:var(--ink)}
.post-card h4{margin-top:16px;font-size:17px;font-weight:700;letter-spacing:.2px}
.post-card p{margin-top:12px;font-size:12.5px;line-height:24px;color:var(--muted)}
.post-card .btn{left:32px;bottom:30px;width:109px;height:39px}

/* contact */
.field{position:absolute;border:1.5px solid rgba(255,255,255,.75);color:var(--white);font-size:13.5px;padding:0 26px;display:flex;align-items:center}
.field.tall{align-items:flex-start;padding-top:22px}
.submit{background:var(--white);color:var(--ink)}

/* footer */
.footer-nav{position:absolute;top:3898px;left:143px;font-size:17px;color:var(--ink);word-spacing:2px}
.footer-nav span{margin:0 26px}
.social{position:absolute;top:3893px;width:34px;height:34px;border-radius:50%;background:var(--ink)}
.legal{position:absolute;left:143px;top:3945px;font-size:12.5px;color:var(--muted)}
</style>
</head>
<body>

<svg class="bands" viewBox="0 0 1200 4000" aria-hidden="true">
  <defs>
    <linearGradient id="heroFill" x1="0" y1="0" x2="1" y2="1">
      <stop offset="0" stop-color="#8a8a8a"/>
      <stop offset=".5" stop-color="#5a5a5a"/>
      <stop offset="1" stop-color="#2e2e2e"/>
    </linearGradient>
    <linearGradient id="stoneFill" x1="0" y1="0" x2="0" y2="1">
      <stop offset="0" stop-color="#f3f3f3"/>
      <stop offset=".55" stop-color="#e6e6e6"/>
      <stop offset="1" stop-color="#c9c9c9"/>
    </linearGradient>
    <linearGradient id="nightFill" x1="0" y1="0" x2="0" y2="1">
      <stop offset="0" stop-color="#0d0d0d"/>
      <stop offset=".5" stop-color="#1d1d1d"/>
      <stop offset="1" stop-color="#0a0a0a"/>
    </linearGradient>
  </defs>
  <path d="M0,272 Q600,16 1200,256 L1200,753 Q600,1033 0,753 Z" fill="url(#heroFill)"/>
  <path d="M170,190 Q640,40 1200,262" fill="none" stroke="#000" stroke-width="5"/>
  <path d="M60,790 Q600,1050 1150,790" fill="none" stroke="#000" stroke-width="6"/>

  <path d="M0,1662 Q600,1428 1200,1662 L1200,2128 Q600,2344 0,2128 Z" fill="url(#stoneFill)"/>
  <path d="M160,1598 Q640,1465 1200,1668" fill="none" stroke="#000" stroke-width="4"/>
  <path d="M100,2172 Q620,2360 1110,2172" fill="none" stroke="#000" stroke-width="5"/>

  <path d="M0,3121 Q600,2859 1200,3121 L1200,3548 Q600,3814 0,3548 Z" fill="url(#nightFill)"/>
  <path d="M170,3050 Q640,2880 1200,3110" fill="none" stroke="#000" stroke-width="5"/>
  <path d="M90,3600 Q610,3830 1130,3600" fill="none" stroke="#000" stroke-width="5"/>
</svg>

<!-- header -->
<div class="brand" style="left:140px;top:8px;width:220px">
  <span class="brand-mark" style="width:64px;height:64px;margin-bottom:14px"></span>
  <span class="brand-name">THE WILLOW</span>
  <span class="brand-sub">HOURS</span>
</div>
<div class="phone" style="left:722px;top:17px">
  <span class="phone-icon"><svg width="16" height="16" viewBox="0 0 24 24"><path fill="#fff" d="M6.6 10.8a15.1 15.1 0 0 0 6.6 6.6l2.2-2.2a1 1 0 0 1 1-.25 11.4 11.4 0 0 0 3.6.57 1 1 0 0 1 1 1V20a1 1 0 0 1-1 1A17 17 0 0 1 3 4a1 1 0 0 1 1-1h3.5a1 1 0 0 1 1 1c0 1.25.2 2.45.57 3.57a1 1 0 0 1-.25 1z"/></svg></span>
  +1 555 010 2040
</div>
<div class="btn" style="left:950px;top:12px;width:105px;height:40px">Schedule</div>
<nav class="nav">
  <a style="left:0;top:0">HOME</a>
  <a style="left:70px;top:0">BLOG</a>
  <a style="left:135px;top:0">SERVICES</a>
  <a style="left:230px;top:0">ABOUT</a>
  <a style="left:305px;top:0">CONTACT</a>
</nav>
<svg class="cart" width="34" height="30" viewBox="0 0 34 30" aria-label="Cart">
  <path d="M2 5h5l3.5 14h15l3-10H9" fill="none" stroke="#111" stroke-width="2.2" stroke-linejoin="round"/>
  <circle cx="12" cy="24" r="2.2" fill="#111"/><circle cx="24" cy="24" r="2.2" fill="#111"/>
  <circle cx="29" cy="5" r="5" fill="#111"/><text x="29" y="8" font-size="8" font-family="Roboto,sans-serif" fill="#fff" text-anchor="middle">0</text>
</svg>

<!-- hero -->
<div class="abs" style="left:0;top:140px;width:1200px;height:760px;pointer-events:none" role="img" aria-label="Sunlit field of tall grass in soft grey tones"></div>
<div class="abs" style="left:443px;top:225px;width:310px;height:310px;border-radius:50%;border:2px solid rgba(255,255,255,.9)"></div>
<div class="hero-title" style="top:608px">
  <span class="big">THE WILLOW</span>
  <span class="small">HOURS</span>
</div>

<!-- about -->
<div class="about-ring"></div>
<div class="about-photo" role="img" aria-label="Two women talking across a desk by a bright window"></div>
<h2 class="about-title"><span class="dash"></span>ABOUT<span class="dash"></span></h2>
<p class="about-text">Lorem ipsum dolor sit amet, consectetur adipiscing elit, sed do eiusmod tempor incididunt ut labore et dolore magna aliquais ipsum suspendisse ultrices gravida. Risus commodo viverra maecenas accumsan lacus vel facilisis. Lorem ipsum dolor sit amet, consectetur adipiscing elit, sed do eiusmod tempor incididunt udolore magna aliquais ipsum suspendisse ultrices gravida. Risus commodo viverra maecenas accumsan lacus vel facilisis. Lorem ipsum dolor sit amet, consectetur adipiscing elit, sed do eiusmod tempor incididt dolore magna aliquais ipsum suspendisse ultrices gravida. Risus commodo viverra maecenas accumsan lacus vel facilisis. Lorem ipsum dolor sit amet, consectetur adipiscing elit, sed do eiusmod tempor incididunt ut labore et dolore magna aliquais ipsum suspendisse ultricsus commodo viverra maecenas accumsan lacus vel facilisis.</p>
<div class="btn" style="left:601px;top:1421px;width:107px;height:40px">Read More</div>

<!-- services -->
<div class="abs" style="left:0;top:1545px;width:1200px;height:700px;pointer-events:none" role="img" aria-label="Soft misty backdrop of stacked pebbles"></div>
<h2 class="section-title" style="top:1678px"><span class="dash"></span>SERVICES<span class="dash"></span></h2>

<div class="service" style="left:144px;top:1795px">
  <svg class="service-icon" width="60" height="60" viewBox="0 0 60 60" fill="none" stroke="#111" stroke-width="2.4">
    <circle cx="20" cy="14" r="6"/><circle cx="40" cy="14" r="6"/>
    <path d="M10 36v-8a8 8 0 0 1 16 0v8M34 36v-8a8 8 0 0 1 12 0v8"/>
    <path d="M6 38h48M12 38v16M48 38v16"/>
  </svg>
  <h3>VOLUPTATEM</h3>
  <p>Lorem ipsum dolor sit amet, consectetur adipiscing elit, sed do eiusmod tempor incididunt ut labore et dolore</p>
  <span class="service-arrow"><svg width="20" height="20" viewBox="0 0 20 20"><circle cx="10" cy="10" r="8" fill="none" stroke="#fff" stroke-width="1.6"/><path d="M6 10h8M11 7l3 3-3 3" fill="none" stroke="#fff" stroke-width="1.6"/></svg></span>
</div>

<div class="service" style="left:457px;top:1795px">
  <svg class="service-icon" width="60" height="60" viewBox="0 0 60 60" fill="none" stroke="#111" stroke-width="2.4">
    <rect x="4" y="6" width="18" height="14" rx="2"/><circle cx="46" cy="12" r="8"/>
    <circle cx="30" cy="40" r="8"/><circle cx="30" cy="40" r="3"/>
    <rect x="42" y="38" width="14" height="12" rx="2"/>
    <path d="M8 44c0-4 2-6 4-6M12 54v-2"/>
  </svg>
  <h3>DUIS AUTE</h3>
  <p>Lorem ipsum dolor sit amet, consectetur adipiscing elit, sed do eiusmod tempor incididunt ut labore et dolore</p>
  <span class="service-arrow"><svg width="20" height="20" viewBox="0 0 20 20"><circle cx="10" cy="10" r="8" fill="none" stroke="#fff" stroke-width="1.6"/><path d="M6 10h8M11 7l3 3-3 3" fill="none" stroke="#fff" stroke-width="1.6"/></svg></span>
</div>

<div class="service" style="left:770px;top:1795px">
  <svg class="service-icon" width="60" height="60" viewBox="0 0 60 60" fill="none" stroke="#111" stroke-width="2.4">
    <rect x="20" y="4" width="20" height="14" rx="1"/>
    <circle cx="10" cy="16" r="5"/><circle cx="50" cy="16" r="5"/>
    <path d="M4 32h52M10 32v22M50 32v22M22 32v14h16V32"/>
  </svg>
  <h3>UT ENIM AD</h3>
  <p>Lorem ipsum dolor sit amet, consectetur adipiscing elit, sed do eiusmod tempor incididunt ut labore et dolore</p>
  <span class="service-arrow"><svg width="20" height="20" viewBox="0 0 20 20"><circle cx="10" cy="10" r="8" fill="none" stroke="#fff" stroke-width="1.6"/><path d="M6 10h8M11 7l3 3-3 3" fill="none" stroke="#fff" stroke-width="1.6"/></svg></span>
</div>

<!-- blog -->
<h2 class="section-title" style="top:2354px"><span class="dash"></span>BLOG POSTS<span class="dash"></span></h2>

<div class="post-photo" style="left:144px;top:2475px;background:linear-gradient(90deg,#dedede,#f2f2f2 55%,#d2d2d2)" role="img" aria-label="Two women in conversation in a bright room"></div>
<article class="post-card" style="left:179px;top:2671px">
  <div class="post-meta"><svg width="13" height="13" viewBox="0 0 14 14"><rect x="1" y="2.5" width="12" height="10.5" fill="none" stroke="#111" stroke-width="1.5"/><path d="M1 6h12M4 1v3M10 1v3" stroke="#111" stroke-width="1.5"/></svg>October 2022&nbsp;|&nbsp;Comments</div>
  <h4>RCHITECTO BEATAE VITAE DICTA</h4>
  <p>Lorem ipsum dolor sit amet, consectetur adipiscing elit, sed do eiusmod tempor incididunt ut labore et dolore magna aliqupsum suspendisse</p>
  <div class="btn">Read More</div>
</article>

<div class="post-photo" style="left:616px;top:2475px;background:linear-gradient(135deg,#c9c9c9,#8c8c8c 55%,#2e2e2e)" role="img" aria-label="Hands with a pen over a notebook at a table meeting"></div>
<article class="post-card" style="left:651px;top:2671px">
  <div class="post-meta"><svg width="13" height="13" viewBox="0 0 14 14"><rect x="1" y="2.5" width="12" height="10.5" fill="none" stroke="#111" stroke-width="1.5"/><path d="M1 6h12M4 1v3M10 1v3" stroke="#111" stroke-width="1.5"/></svg>October 2022&nbsp;|&nbsp;Comments</div>
  <h4>RCHITECTO BEATAE VITAE DICTA</h4>
  <p>Lorem ipsum dolor sit amet, consectetur adipiscing elit, sed do eiusmod tempor incididunt ut labore et dolore magna aliqupsum suspendisse</p>
  <div class="btn">Read More</div>
</article>

<!-- contact -->
<div class="abs" style="left:0;top:2990px;width:1200px;height:690px;pointer-events:none" role="img" aria-label="Dim backdrop of stacked stones and a cup"></div>
<h2 class="section-title" style="top:3153px;color:var(--white)"><span class="dash"></span>CONTACT<span class="dash"></span></h2>
<div class="field" style="left:183px;top:3277px;width:272px;height:51px">Enter Name</div>
<div class="field" style="left:464px;top:3277px;width:272px;height:51px">Enter Email</div>
<div class="field" style="left:745px;top:3277px;width:272px;height:51px">Phone</div>
<div class="field tall" style="left:183px;top:3344px;width:834px;height:89px">Message</div>
<div class="btn submit" style="left:545px;top:3471px;width:109px;height:42px">Submit</div>

<!-- footer -->
<div class="brand" style="left:493px;top:3718px;width:220px">
  <span class="brand-mark" style="width:62px;height:62px;margin-bottom:12px"></span>
  <span class="brand-name" style="font-size:22px">THE WILLOW</span>
  <span class="brand-sub" style="font-size:11px">HOURS</span>
</div>
<div class="phone" style="left:820px;top:3781px;font-size:25px">
  <span class="phone-icon" style="width:36px;height:36px"><svg width="19" height="19" viewBox="0 0 24 24"><path fill="#fff" d="M6.6 10.8a15.1 15.1 0 0 0 6.6 6.6l2.2-2.2a1 1 0 0 1 1-.25 11.4 11.4 0 0 0 3.6.57 1 1 0 0 1 1 1V20a1 1 0 0 1-1 1A17 17 0 0 1 3 4a1 1 0 0 1 1-1h3.5a1 1 0 0 1 1 1c0 1.250.2 2.45.57 3.57a1 1 0 0 1-.25 1z"/></svg></span>
  +1 555 010 2040
</div>
<div class="footer-nav">HOME<span>/</span>BLOG<span>/</span>SERVICES<span>/</span>ABOUT<span>/</span>CONTACT</div>
<span class="social" style="left:923px" role="img" aria-label="Social link"></span>
<span class="social" style="left:972px" role="img" aria-label="Social link"></span>
<span class="social" style="left:1020px" role="img" aria-label="Social link"></span>
<div class="legal">© 2022 The Willow Hours. All rights reserved.Privacy &nbsp;|&nbsp; Terms of Use</div>

</body>
</html>
```